Simple Slide from Excel on History of Technology

I need to convert this timeline into a more readable and friendly slide for a report I am doing. It is in Excel format. Feel free to cut some of the words and make it more simple. It can be in Word, powerpoint or excel.

Target Market(s)

a school paper, a professor will see

Requirements
Must have
• should give a feeling of momentum over time. Please add the number of internet users for each year it is available as 1,000 in 1975, 30,000 in 1987, 14 million in 1993, 25 million in 1994, 45 million in 1995, 77 million in 1996, 121 million in 1997, 188 million in 1998, 281 million in 1999, 413 million in 2000, 910 million in 2004, 1.4 billion in 2007

```html
<!DOCTYPE html>
<html lang="en">
<head>
<meta charset="utf-8">
<title>History of the Internet Timeline</title>
<link href="https://fonts.googleapis.com/css2?family=Carlito:ital,wght@0,400;0,700;1,400&display=swap" rel="stylesheet">
<style>
  :root {
    --sixties: #4a7ebb;
    --seventies: #c0504d;
    --eighties: #9bbb59;
    --nineties: #8064a2;
    --two-thousands: #4bacc6;
    --ink: #404040;
    --axis: #7f7f7f;
    --area: #e3e3e3;
    --paper: #ffffff;
  }
  * { margin: 0; padding: 0; box-sizing: border-box; }
  html, body { width: 1200px; height: 900px; overflow: hidden; background: var(--paper); }
  body { font-family: "Carlito", "Calibri", sans-serif; color: var(--ink); }
  .timeline { position: relative; width: 1200px; height: 900px; }
  .chart { position: absolute; left: 0; top: 0; }
  .column { position: absolute; font-size: 13.5px; line-height: 17px; }
  .event-year { font-size: 19px; line-height: 22px; font-weight: 700; margin-top: 7px; }
  .event-year:first-child { margin-top: 0; }
  .event-text { margin-top: 2px; }
  .event-text em { font-style: italic; }
  .c60 .event-year { color: var(--sixties); }
  .c70 .event-year { color: var(--seventies); }
  .c80 .event-year { color: var(--eighties); }
  .c90 .event-year { color: var(--nineties); }
  .c00 .event-year { color: var(--two-thousands); }
  .credit { position: absolute; right: 40px; top: 866px; font-size: 11px; font-style: italic; color: var(--ink); }
  .credit b { font-weight: 700; }
</style>
</head>
<body>
<div class="timeline">
  <svg class="chart" width="1200" height="900" viewBox="0 0 1200 900" role="img" aria-label="Internet users growing from 1,000 in 1975 to 1.4 billion in 2007">
    <polygon fill="var(--area)" points="277,447 277,391 495,369 612,330 679,302 737,275 790,229 842,181 895,142 950,116 1032,95 1085,65 1141,34 1141,447"/>
    <text x="850" y="328" font-size="19" font-weight="700" fill="var(--ink)" font-family="Carlito, sans-serif">INTERNET USERS</text>

    <g stroke-width="1.3">
      <line x1="100" y1="335" x2="100" y2="447" stroke="var(--sixties)"/>
      <line x1="368" y1="447" x2="368" y2="335" stroke="var(--eighties)"/>
      <line x1="272" y1="335" x2="563" y2="335" stroke="var(--eighties)"/>
      <line x1="194" y1="447" x2="194" y2="516" stroke="var(--seventies)"/>
      <line x1="22" y1="516" x2="385" y2="516" stroke="var(--seventies)"/>
      <line x1="576" y1="447" x2="576" y2="516" stroke="var(--nineties)"/>
      <line x1="429" y1="516" x2="791" y2="516" stroke="var(--nineties)"/>
      <line x1="1032" y1="447" x2="1032" y2="516" stroke="var(--two-thousands)"/>
      <line x1="889" y1="516" x2="1166" y2="516" stroke="var(--two-thousands)"/>
    </g>

    <line x1="42" y1="447" x2="1160" y2="447" stroke="var(--axis)" stroke-width="3"/>
    <circle cx="42" cy="447" r="5" fill="var(--axis)"/>
    <circle cx="1160" cy="447" r="5" fill="var(--axis)"/>
    <circle cx="100" cy="447" r="9" fill="var(--sixties)"/>
    <circle cx="194" cy="447" r="9" fill="var(--seventies)"/>
    <circle cx="368" cy="447" r="9" fill="var(--eighties)"/>
    <circle cx="576" cy="447" r="9" fill="var(--nineties)"/>
    <circle cx="1032" cy="447" r="9" fill="var(--two-thousands)"/>

    <g font-family="Carlito, sans-serif" font-weight="700" font-size="30">
      <text x="62" y="495" fill="var(--sixties)">1960s</text>
      <text x="148" y="424" fill="var(--seventies)">1970s</text>
      <text x="328" y="495" fill="var(--eighties)">1980s</text>
      <text x="538" y="424" fill="var(--nineties)">1990s</text>
      <text x="988" y="424" fill="var(--two-thousands)">2000s</text>
    </g>

    <g>
      <circle cx="277" cy="391" r="9" fill="var(--seventies)"/>
      <circle cx="495" cy="369" r="9" fill="var(--eighties)"/>
      <circle cx="612" cy="330" r="8" fill="var(--nineties)"/>
      <circle cx="679" cy="302" r="8" fill="var(--nineties)"/>
      <circle cx="737" cy="275" r="8" fill="var(--nineties)"/>
      <circle cx="790" cy="229" r="8" fill="var(--nineties)"/>
      <circle cx="842" cy="181" r="8" fill="var(--nineties)"/>
      <circle cx="895" cy="142" r="8" fill="var(--nineties)"/>
      <circle cx="950" cy="116" r="8" fill="var(--nineties)"/>
      <circle cx="1032" cy="95" r="8" fill="var(--two-thousands)"/>
      <circle cx="1085" cy="65" r="8" fill="var(--two-thousands)"/>
      <circle cx="1141" cy="34" r="8" fill="var(--two-thousands)"/>
    </g>

    <g font-family="Carlito, sans-serif" font-size="13.5">
      <text x="258" y="426" fill="var(--seventies)" font-weight="700" font-size="15">1975</text>
      <text x="273" y="441" fill="var(--ink)">1K</text>
      <text x="475" y="403" fill="var(--eighties)" font-weight="700" font-size="15">1987</text>
      <text x="488" y="418" fill="var(--ink)">30K</text>
      <g fill="var(--nineties)" font-weight="700" font-size="15">
        <text x="602" y="358">1993</text>
        <text x="670" y="330">1994</text>
        <text x="718" y="307">1995</text>
        <text x="772" y="260">1996</text>
        <text x="824" y="212">1997</text>
        <text x="877" y="174">1998</text>
        <text x="932" y="147">1999</text>
      </g>
      <g fill="var(--nineties)">
        <text x="604" y="374">14Mil</text>
        <text x="666" y="351">25Mil</text>
        <text x="721" y="322">45Mil</text>
        <text x="775" y="275">77Mil</text>
        <text x="823" y="228">121Mil</text>
        <text x="876" y="189">188Mil</text>
        <text x="934" y="162">281Mil</text>
      </g>
      <g fill="var(--two-thousands)" font-weight="700" font-size="15">
        <text x="1013" y="127">2000</text>
        <text x="1063" y="98">2004</text>
        <text x="1118" y="64">2007</text>
      </g>
      <g fill="var(--two-thousands)">
        <text x="1013" y="143">413Mil</text>
        <text x="1063" y="113">910Mil</text>
        <text x="1118" y="80">1.4Bil</text>
      </g>
    </g>
  </svg>

  <div class="column c60" style="left:72px; top:250px; width:90px;">
    <p class="event-year">1969</p>
    <p class="event-text">First Network - Unilink</p>
  </div>

  <div class="column c80" style="left:198px; top:22px; width:180px;">
    <p class="event-year">1982</p>
    <p class="event-text">First emoticon :-), a smiley face by Samuel Farrow</p>
    <p class="event-year">1983</p>
    <p class="event-text">Unilink switch to TCP/IP</p>
    <p class="event-year">1984</p>
    <p class="event-text">Domain Name System created, www.example.com, links user friendly names to IP addresses</p>
    <p class="event-year">1987</p>
    <p class="event-text">30,000 hosts on the Internet having grown from 1,000 limit by Unilink</p>
  </div>

  <div class="column c80" style="left:386px; top:22px; width:185px;">
    <p class="event-year">1988</p>
    <p class="event-text">Internet Relay Chat created, set up capability for real-time chat, instant messaging. Also, first malicious internet based attack "<em>the harlow worm</em>" occurred.</p>
    <p class="event-year" style="margin-top:12px;">1989</p>
    <p class="event-text">NetHome is launched, increased popularity of the internet across average users. Tom Bradley-Lane proposed the world wide web at the Geneva Lab</p>
  </div>

  <div class="column c70" style="left:35px; top:526px; width:150px;">
    <p class="event-year">1970</p>
    <p class="event-text">Unilink expanded to Universities</p>
    <p class="event-year">1971</p>
    <p class="event-text">Email developed by Roy Tamsin. First used @ symbol</p>
    <p class="event-year">1973</p>
    <p class="event-text">First connection outside the U.S. - Northbridge College</p>
    <p class="event-year">1974</p>
    <p class="event-text">The Beginning of TCP/IP (transmission control protocol), links Unilink networks with no central control</p>
  </div>

  <div class="column c70" style="left:227px; top:526px; width:160px;">
    <p class="event-year">1975</p>
    <p class="event-text">First Email program - added Reply and Forward capability</p>
    <p class="event-year">1976</p>
    <p class="event-text">PC Modem created for computer hobbyists</p>
    <p class="event-year">1978</p>
    <p class="event-text">First Spam email sent by Gerald Thorne to Unilink Users</p>
    <p class="event-year">1979</p>
    <p class="event-text">Earliest form of multiplayer games, all text</p>
  </div>

  <div class="column c90" style="left:432px; top:526px; width:175px;">
    <p class="event-year">1991</p>
    <p class="event-text">Tom Bradley-Lane wrote the code for world wide web (WWW). First web page created. First search protocol, set up search engines. First webcam.</p>
    <p class="event-year">1993</p>
    <p class="event-text">First graphical web browser to make the internet easy to use for non-techies</p>
  </div>

  <div class="column c90" style="left:622px; top:526px; width:180px;">
    <p class="event-year">1994</p>
    <p class="event-text">First .org and .gov sites for nonprofits and the government's general use. Wayfarer Navigator launched, a much easier web browser. Became a standard.</p>
    <p class="event-year">1995</p>
    <p class="event-text">Commercialization of the internet, SSL (secure sockets layer) encryption made it safer to conduct financial transactions.</p>
    <p class="event-year">1998</p>
    <p class="event-text">Seekly went live!</p>
  </div>

  <div class="column c00" style="left:907px; top:526px; width:140px;">
    <p class="event-year">2001</p>
    <p class="event-text">OpenPedia launched.</p>
    <p class="event-year">2004</p>
    <p class="event-text">Circlefeed opens, social media starts.</p>
  </div>

  <div class="column c00" style="left:1062px; top:528px; width:130px;">
    <p class="event-year">2005</p>
    <p class="event-text">ClipStream starts</p>
    <p class="event-year" style="margin-top:3px;">2006</p>
    <p class="event-text">Chirper starts</p>
    <p class="event-year" style="margin-top:3px;">2007</p>
    <p class="event-text">PocketPhone</p>
  </div>

  <p class="credit"><b>Credit:</b> &nbsp;www.timelinehub.com/blog/tech/the-story-of-the-internet-in-brief/</p>
</div>
</body>
</html>
```